I want both print and ebook covers

book title is "The Classroom MEETING HANDBOOK: Fresh Paths to Partner With Families For Pupil Growth. I want a dark Teal or Navy Background. Yellow and white letters. Distorted Picture of one teacher, two parents and one child around a table or desk. But no Martians! My name should include "Award Winning Author"

Target Market(s)

teachers and other educators--principals, school psychologists, speech therapists, etc.

Industry/Entity Type

schools

• I just need to see how it looks

Colors
0054AA
0677BA
7BADD7
CADEEF
E8F1F8
0094D4
00A9DD
6FCCEA
C7EBF8
E9F6FB
FFC000
F8CF3A
FAE287
FDF2CF
FEFAEE

Requirements
Must have
• Title top third of page big enough to be read when reduced greatly in size. Contrast so that it "pops'.
Nice to have
• Teacher, two parents and one child around a table/desk. My name should include 'Award winning author'

```html
<!DOCTYPE html>
<html lang="en">
<head>
<meta charset="utf-8">
<title>The Classroom Meeting Handbook – Cover</title>
<link rel="stylesheet" href="https://fonts.googleapis.com/css2?family=Archivo:wght@800&display=swap">
<style>
  :root {
    --page-bg: #e9e9e9;
    --navy: #0054aa;
    --ocean: #0677ba;
    --white: #ffffff;
    --sun: #f8cf3a;
    --coral: #e0607a;
    --sand: #fae287;
    --sage: #c5d3b8;
  }
  html, body {
    margin: 0;
    padding: 0;
    width: 1200px;
    height: 1200px;
    overflow: hidden;
    background: var(--page-bg);
  }
  .stage {
    position: relative;
    width: 1200px;
    height: 1200px;
  }
  .book-cover {
    position: absolute;
    left: 254px;
    top: 80px;
    width: 692px;
    height: 1039px;
    display: block;
  }
  .cover-title,
  .author-line {
    font-family: "Archivo", "Helvetica Neue", Arial, sans-serif;
    font-weight: 800;
  }
  .title-white { fill: var(--white); }
  .title-yellow { fill: var(--sun); }
  .author-line { fill: var(--white); }
</style>
</head>
<body>
<div class="stage">
  <svg class="book-cover" viewBox="0 0 692 1039" xmlns="http://www.w3.org/2000/svg">
    <defs>
      <linearGradient id="scene-tones" x1="0" y1="0" x2="1" y2="1">
        <stop offset="0" stop-color="#f6c47a"/>
        <stop offset="0.55" stop-color="#e98a86"/>
        <stop offset="1" stop-color="#c9d4b8"/>
      </linearGradient>
    </defs>

    <!-- background bands -->
    <rect class="cover-sky" x="0" y="0" width="692" height="767" fill="var(--navy)"/>
    <rect class="cover-floor" x="0" y="767" width="692" height="272" fill="var(--ocean)"/>

    <!-- title -->
    <g class="cover-title" text-anchor="middle">
      <text class="title-white" x="346" y="95" font-size="60" textLength="118" lengthAdjust="spacingAndGlyphs">THE</text>
      <text class="title-white" x="345" y="190" font-size="116" textLength="607" lengthAdjust="spacingAndGlyphs">CLASSROOM</text>
      <text class="title-yellow" x="345" y="328" font-size="160" textLength="607" lengthAdjust="spacingAndGlyphs">MEETING</text>
      <text class="title-white" x="345" y="465" font-size="150" textLength="607" lengthAdjust="spacingAndGlyphs">HANDBOOK</text>
    </g>

    <!-- illustration area -->
    <rect class="meeting-scene" role="img"
          aria-label="Illustration of a teacher at a desk with a laptop and plant, talking with a parent and child seated in pink chairs, with confetti stars above"
          x="41" y="519" width="607" height="440" rx="18"
          fill="url(#scene-tones)" opacity="0.85"/>

    <!-- author -->
    <text class="author-line" x="346" y="1018" font-size="44" text-anchor="middle" textLength="491" lengthAdjust="spacingAndGlyphs">AWARD WINNING AUTHOR</text>
  </svg>
</div>
</body>
</html>
```